Business card with logo for a family psychologist

I need a business card for my private practice in the urban Chicago area as a psychologist. I see families and individuals who are going through difficult times - divorce, separation, illness, or trauma. I want to project hopefulness, competence, and caring.

Target Market(s)

Adults, other professionals - such as physicans and lawyers

Industry/Entity Type

Health Care

Contact Information for Business Card

Front should have my name and credentials; back should have location information including my email, phone

Font styles to use
Serif
Decorative
Script

Requirements
Must have
• Unique logo
Should not have
• No pictures or icons of people; no black

```html
<!DOCTYPE html>
<html lang="en">
<head>
<meta charset="utf-8">
<title>Dr. Dana Whitfield – Business Card</title>
<link rel="stylesheet" href="https://fonts.googleapis.com/css2?family=Caladea:wght@400;700&display=swap">
<style>
  :root {
    --orange-deep: #db4510;
    --orange: #f25d24;
    --orange-soft: #f79a76;
    --white: #ffffff;
    --ink: #2b2b2b;
    --ink-soft: #4a4a4a;
  }
  * { box-sizing: border-box; margin: 0; padding: 0; }
  html, body { width: 1200px; height: 954px; overflow: hidden; background: var(--white); }
  body { position: relative; font-family: "Caladea", Georgia, serif; }

  .card {
    position: absolute; top: 18px; width: 552px; height: 919px;
    background: var(--orange-deep); border-radius: 41px;
  }
  .card--back { left: 34px; }
  .card--front { left: 613px; }

  .card__panel {
    position: absolute; left: 14px; right: 14px; top: 23px; bottom: 22px;
    border-radius: 33px; overflow: hidden;
  }
  .card--back .card__panel { background: var(--white); }
  .card--front .card__panel { background: var(--orange); border: 1.5px solid var(--white); }

  .header-band {
    position: absolute; left: 0; right: 0; top: 0; height: 282px;
    background: var(--orange); border: 1.5px solid var(--white); border-bottom: none;
    border-radius: 33px 33px 0 0;
  }

  .centered { position: absolute; left: 0; right: 0; text-align: center; color: var(--white); }

  .brand {
    display: flex; align-items: center; justify-content: center; gap: 8px;
    font-size: 15px; letter-spacing: 1px; color: var(--white);
  }
  .brand__dot { width: 12px; height: 12px; border-radius: 50%; background: var(--orange-soft); }

  .title-name { font-weight: 400; letter-spacing: .5px; line-height: 1; }
  .rule { position: absolute; height: 1.5px; background: var(--orange-soft); }
  .subtitle { line-height: 1; }

  .header-band .brand-wrap { top: 70px; }
  .header-band .title-name { top: 142px; font-size: 36px; }
  .header-band .rule { top: 192px; left: 119px; width: 287px; }
  .header-band .subtitle { top: 213px; font-size: 18px; }

  .card--front .brand-wrap { top: 330px; }
  .card--front .brand { font-size: 20px; }
  .card--front .brand__dot { width: 16px; height: 16px; }
  .card--front .title-name { top: 436px; font-size: 52px; }
  .card--front .rule { top: 513px; left: 50px; width: 427px; }
  .card--front .subtitle { top: 542px; font-size: 27px; }

  .identity { position: absolute; left: 48px; top: 388px; }
  .identity__name { font-size: 25px; font-weight: 400; color: var(--ink); letter-spacing: .5px; line-height: 1; }
  .identity__role { margin-top: 11px; font-size: 16px; color: var(--ink-soft); line-height: 1; }
  .identity__rule { margin-top: 11px; width: 123px; height: 2px; background: var(--orange); }

  .contact { position: absolute; left: 49px; right: 20px; height: 51px; display: flex; align-items: center; }
  .contact__icon {
    width: 51px; height: 51px; border-radius: 50%; flex: none;
    background: linear-gradient(160deg, var(--orange), var(--orange-deep));
    display: flex; align-items: center; justify-content: center;
  }
  .contact__text { margin-left: 39px; font-size: 17.5px; color: var(--ink-soft); line-height: 1.35; letter-spacing: .2px; }
  .contact--address { top: 510px; }
  .contact--phone { top: 600px; }
  .contact--email { top: 690px; }
</style>
</head>
<body>
  <section class="card card--back">
    <div class="card__panel">
      <header class="header-band">
        <div class="centered brand-wrap"><div class="brand"><span class="brand__dot"></span>Whitfield Psychology</div></div>
        <h1 class="centered title-name">DR. DANA WHITFIELD</h1>
        <div class="rule"></div>
        <p class="centered subtitle">Licensed Clinical Psychologist</p>
      </header>

      <div class="identity">
        <h2 class="identity__name">DANA WHITFIELD, PH.D.</h2>
        <p class="identity__role">Licensed Clinical Psychologist</p>
        <div class="identity__rule"></div>
      </div>

      <div class="contact contact--address">
        <span class="contact__icon">
          <svg width="18" height="26" viewBox="0 0 18 26" aria-hidden="true">
            <path d="M9 1C4.6 1 1 4.6 1 9c0 6 8 16 8 16s8-10 8-16c0-4.4-3.6-8-8-8z" fill="#fff"/>
            <circle cx="9" cy="9" r="3.6" fill="#e8501a"/>
          </svg>
        </span>
        <p class="contact__text">240 N. Lakeview Suite 815<br>Chicago, Illinois 60611</p>
      </div>

      <div class="contact contact--phone">
        <span class="contact__icon">
          <svg width="24" height="18" viewBox="0 0 24 18" aria-hidden="true">
            <path d="M1 6c0-3 5-5 11-5s11 2 11 5v1.5h-5V5c-2-.8-10-.8-12 0v2.5H1z" fill="#fff"/>
            <path d="M6 7h12l3 8v2H3v-2z" fill="#fff"/>
            <circle cx="12" cy="12" r="2.5" fill="#e8501a"/>
          </svg>
        </span>
        <p class="contact__text">312-555-0147</p>
      </div>

      <div class="contact contact--email">
        <span class="contact__icon">
          <svg width="24" height="16" viewBox="0 0 24 16" aria-hidden="true">
            <rect x="1" y="1" width="22" height="14" fill="#fff"/>
            <path d="M1 1l11 8 11-8M1 15l8-7M23 15l-8-7" fill="none" stroke="#e8501a" stroke-width="1.3"/>
          </svg>
        </span>
        <p class="contact__text">drdanawhitfield@mailhaven.com</p>
      </div>
    </div>
  </section>

  <section class="card card--front">
    <div class="card__panel">
      <div class="centered brand-wrap"><div class="brand"><span class="brand__dot"></span>Whitfield Psychology</div></div>
      <h1 class="centered title-name">DR. DANA WHITFIELD</h1>
      <div class="rule"></div>
      <p class="centered subtitle">Licensed Clinical Psychologist</p>
    </div>
  </section>
</body>
</html>
```